ALL TEXT Social Media Graphics

We are looking for a series of social media graphics for Instagram (new size: 4:5 (1080 x 1350 pixels) ratio that are ALL TEXT. We want the following quotes below on each graphic; one quote per graphic. AND, In very small letters at the bottom of each graphic, add @PaulaWrenLive
The look and feel of these graphics should be complimentary to the color palette attached below; but keep them simple. But the design is up to you; at the end of this document, I provided various samples of all text graphics that I like as examples.
The Quotes are in the attached WORD document
women trying to lose weight

```html
<!DOCTYPE html>
<html lang="en">
<head>
<meta charset="utf-8">
<title>Summer Slimdown Quote Graphics</title>
<link rel="stylesheet" href="https://fonts.googleapis.com/css2?family=Fredoka:wght@600;700&family=Roboto:wght@300;500;700&display=swap">
<style>
  :root {
    --backdrop: #1c0511;
    --frame: #ffffff;
    --panel-top: #fdf0f5;
    --panel-bottom: #fadbe6;
    --ink: #c12f6c;
    --pill: #f06394;
    --pill-ink: #ffffff;
    --soft-ink: #c8457c;
  }
  * { box-sizing: border-box; margin: 0; padding: 0; }
  html, body { width: 1200px; height: 600px; overflow: hidden; background: var(--backdrop); }
  .board {
    position: relative;
    width: 1200px; height: 600px;
    display: grid;
    grid-template-columns: repeat(5, 221px);
    grid-template-rows: repeat(2, 276px);
    column-gap: 11.5px;
    row-gap: 16px;
    padding: 11px 0 0 23px;
  }
  .card { background: var(--frame); padding: 6px; }
  .panel {
    height: 100%;
    background: linear-gradient(180deg, var(--panel-top), var(--panel-bottom));
    display: flex; flex-direction: column;
    padding: 18px 5px 10px;
  }
  .headline {
    margin-left: 8px;
    border-left: 1px solid var(--ink);
    padding: 2px 2px 4px 6px;
    font-family: "Roboto", sans-serif;
    font-weight: 700;
    font-size: 16px;
    line-height: 1.15;
    color: var(--ink);
  }
  .headline .small { font-size: 14px; }
  .pill {
    margin-top: 4px;
    background: var(--pill);
    color: var(--pill-ink);
    border-radius: 16px;
    padding: 8px 4px;
    text-align: center;
    font-family: "Fredoka", sans-serif;
    font-weight: 700;
    font-variant: small-caps;
    font-size: 18px;
    line-height: 0.98;
    letter-spacing: 0.4px;
  }
  .pill.narrow { margin: 6px 24px 0; font-size: 15px; padding: 8px 2px; }
  .pill.big { font-size: 21px; line-height: 1; padding: 10px 4px; }
  .pill.compact { font-size: 16px; }
  .cta {
    margin-top: 8px;
    text-align: center;
    font-family: "Roboto", sans-serif;
    font-weight: 300;
    font-size: 16.5px;
    line-height: 1.25;
    color: var(--soft-ink);
  }
  .footer {
    margin-top: auto;
    display: flex; align-items: center; gap: 5px;
    padding: 0 8px 8px 13px;
  }
  .footer .rule { flex: 0 0 111px; height: 1px; background: var(--ink); }
  .footer .handle {
    font-family: "Roboto", sans-serif;
    font-weight: 500;
    font-size: 8px;
    color: var(--ink);
    letter-spacing: 0.2px;
  }
</style>
</head>
<body>
<main class="board">

  <article class="card"><div class="panel">
    <p class="headline"><span class="small">You can absolutely be</span><br>down 20–30 pounds<br><span class="small">by end of summer.</span></p>
    <p class="pill">All it takes is<br>the right plan—and<br>you’ve found it.</p>
    <p class="cta">Comment “Sun-Kissed” for the Sun-Kissed Summer Slimdown!</p>
    <div class="footer"><span class="rule"></span><span class="handle">@PaulaWrenLive</span></div>
  </div></article>

  <article class="card"><div class="panel">
    <p class="headline">There’s still time<br>to drop the 30 pounds<br>and slay this summer.</p>
    <p class="pill" style="margin-top:10px;padding:10px 4px">The Sun-Kissed<br>Summer<br>Slimdown has<br>the blueprint.</p>
    <p class="cta" style="margin-top:12px">Comment “Sun-Kissed”!</p>
    <div class="footer"><span class="rule"></span><span class="handle">@PaulaWrenLive</span></div>
  </div></article>

  <article class="card"><div class="panel">
    <p class="headline" style="padding-top:8px;padding-bottom:10px">If your goal is a tiny<br>waist, flat belly,</p>
    <p class="pill" style="padding:10px 4px">And 30 pounds<br>down—this is<br>the plan.</p>
    <p class="cta">Comment “Summer”<br>to join the Sun-Kissed<br>Summer Slimdown!</p>
    <div class="footer"><span class="rule"></span><span class="handle">@PaulaWrenLive</span></div>
  </div></article>

  <article class="card"><div class="panel">
    <p class="headline">This summer ain’t<br>over—and neither<br>are your body goals.</p>
    <p class="pill" style="padding:10px 4px">Drop 30 pounds<br>with the<br>Sun-Kissed Summer<br>Slimdown.</p>
    <p class="cta" style="margin-top:10px">Comment “Sun-Kissed” to<br>get the plan</p>
    <div class="footer"><span class="rule"></span><span class="handle">@PaulaWrenLive</span></div>
  </div></article>

  <article class="card"><div class="panel">
    <p class="headline">You don’t need<br>another diet—you need<br>a system that works.</p>
    <p class="pill" style="padding:10px 4px">Drop 30 pounds<br>with the<br>Sun-Kissed Summer<br>Slimdown.</p>
    <p class="cta" style="margin-top:10px">Comment “Summer”<br>to start now.</p>
    <div class="footer"><span class="rule"></span><span class="handle">@PaulaWrenLive</span></div>
  </div></article>

  <article class="card"><div class="panel">
    <p class="headline" style="padding-bottom:10px">Snatched waist,<br>flat tummy,</p>
    <p class="pill narrow">30 pounds<br>lighter—that’s<br>what the<br>Sun-Kissed<br>Summer Slimdown<br>Challenge<br>delivers.</p>
    <p class="cta">Comment “Sun-Kissed”<br>to get the plan</p>
    <div class="footer"><span class="rule"></span><span class="handle">@PaulaWrenLive</span></div>
  </div></article>

  <article class="card"><div class="panel">
    <p class="headline">You’ve got 8 weeks<br>and the perfect plan<br>to drop 30 pounds.</p>
    <p class="pill" style="margin-top:10px;padding:10px 4px">Let’s get snatched<br>this summer with<br>the Sun-Kissed<br>Summer Slimdown.</p>
    <p class="cta" style="margin-top:12px">Comment “Summer”!</p>
    <div class="footer"><span class="rule"></span><span class="handle">@PaulaWrenLive</span></div>
  </div></article>

  <article class="card"><div class="panel">
    <p class="headline" style="padding-top:10px">Don’t wait ‘til next<br>summer to get right.</p>
    <p class="pill compact" style="padding:9px 4px">The time is<br>now. Drop 30 pounds<br>with the<br>Sun-Kissed Summer<br>Slimdown.</p>
    <p class="cta" style="margin-top:10px">Comment “Summer”!</p>
    <div class="footer"><span class="rule"></span><span class="handle">@PaulaWrenLive</span></div>
  </div></article>

  <article class="card"><div class="panel">
    <p class="headline" style="padding-top:0">Sis, we’re dropping<br>belly flat and saying<br>goodbye to stubborn<br>pounds.</p>
    <p class="pill big">Join the<br>Sun-Kissed Summer</p>
    <p class="cta">Slimdown—comment<br>“Summer”!</p>
    <div class="footer"><span class="rule"></span><span class="handle">@PaulaWrenLive</span></div>
  </div></article>

  <article class="card"><div class="panel">
    <p class="headline" style="padding-top:6px">Nothing feels better<br>than seeing that scale<br>drop week after week.</p>
    <p class="pill" style="margin-top:12px;padding:9px 4px">Let’s lose up to<br>30 pounds this<br>summer—together.</p>
    <p class="cta">Comment “Summer” to<br>join the Sun-Kissed Summer<br>Slimdown!</p>
    <div class="footer"><span class="rule"></span><span class="handle">@PaulaWrenLive</span></div>
  </div></article>

</main>
</body>
</html>
```